New Business Card

Need new business cards like attached. if possible add QR code. Vertical Business Card

I need creative and unique business card design using my company logo. Ok to change logo color. We are a small brokerage doing both Real Estate and Mortgage services. Need to have the follow on business card;
1. agent name - Nora Feldt - Realtor
2. cell - 555-287-4160
3. license number - DRE 07461932
4. business name - Bramwell Nest & Lending, Inc
5. business office - 555-319-8274
6. business address - 238 W. Larkmoor Ave #310, Halden CA 90000
7. business logo - attached (ok to use different color on logo)

```html
<!DOCTYPE html>
<html lang="en">
<head>
<meta charset="utf-8">
<title>Nora Feldt — Business Card</title>
<link rel="stylesheet" href="https://fonts.googleapis.com/css2?family=Arimo:wght@400;700&family=Montserrat:wght@500;600&display=swap">
<style>
  :root {
    --backdrop: #2a2b2d;
    --card: #1c1d1f;
    --card-back-top: #2c2d30;
    --card-back-bottom: #141416;
    --accent: #1aa6f2;
    --accent-deep: #0a6ee0;
    --text: #f2f4f6;
    --rule: #cfd3d8;
  }
  * { box-sizing: border-box; margin: 0; padding: 0; }
  html, body { width: 1200px; height: 1108px; overflow: hidden; }
  body {
    background: var(--backdrop);
    display: flex;
    align-items: center;
    justify-content: center;
    gap: 80px;
    font-family: "Arimo", Arial, sans-serif;
  }
  .card {
    width: 400px;
    height: 660px;
    border-radius: 26px;
    background: var(--card);
    box-shadow: 0 18px 40px rgba(0,0,0,.45);
    position: relative;
    overflow: hidden;
  }
  .card-front {
    display: flex;
    flex-direction: column;
    align-items: center;
    padding: 70px 40px 0;
    color: var(--text);
    text-align: center;
  }
  .brand {
    display: flex;
    flex-direction: column;
    align-items: center;
    gap: 18px;
  }
  .brand-square {
    width: 110px;
    height: 110px;
    background: linear-gradient(135deg, var(--accent), var(--accent-deep));
  }
  .brand-name {
    font-family: "Montserrat", sans-serif;
    font-weight: 600;
    font-size: 15px;
    letter-spacing: 3px;
    color: var(--accent);
    text-transform: uppercase;
    line-height: 1.4;
    text-align: center;
  }
  .brand-name .line-part { display: block; white-space: nowrap; }
  .agent-name {
    margin-top: 34px;
    font-weight: 700;
    font-size: 30px;
    color: var(--accent);
    text-transform: uppercase;
  }
  .agent-role { font-size: 22px; margin-top: 4px; }
  .contact-divider {
    display: flex;
    align-items: center;
    width: 100%;
    gap: 10px;
    margin-top: 14px;
  }
  .contact-divider .line { flex: 1; height: 1px; background: var(--rule); }
  .icon {
    width: 34px; height: 34px;
    border-radius: 7px;
    background: linear-gradient(135deg, var(--accent), var(--accent-deep));
    display: flex; align-items: center; justify-content: center;
  }
  .phones, .address { font-size: 22px; line-height: 1.3; margin-top: 12px; }
  .rule { width: 100%; height: 1px; background: var(--rule); margin-top: 14px; }
  .license { font-size: 22px; margin-top: 14px; }
  .license .label { color: var(--accent); font-weight: 700; }
  .card-back {
    background: linear-gradient(160deg, var(--card-back-top), var(--card-back-bottom));
  }
  .back-pattern { position: absolute; inset: 0; }
  .back-mark {
    position: absolute;
    left: 0; right: 0; bottom: 110px;
    display: flex; flex-direction: column; align-items: center; gap: 10px;
  }
  .back-mark .brand-square { width: 70px; height: 70px; }
  .back-mark .brand-name { font-size: 11px; letter-spacing: 2px; }
</style>
</head>
<body>
  <article class="card card-front">
    <header class="brand">
      <div class="brand-square"></div>
      <div class="brand-name"><span class="line-part">Bramwell Nest</span><span class="line-part">&amp; Lending, Inc</span></div>
    </header>
    <h1 class="agent-name">Nora Feldt</h1>
    <p class="agent-role">Realtor</p>
    <div class="contact-divider">
      <span class="line"></span>
      <span class="icon" aria-label="Office phone">
        <svg width="20" height="20" viewBox="0 0 24 24"><path fill="#fff" d="M6.6 10.8a15 15 0 0 0 6.6 6.6l2.2-2.2c.3-.3.7-.4 1-.2 1.1.4 2.300.6 3.6.6.6 0 1 .4 1 1V20c0 .6-.4 1-1 1A17 17 0 0 1 3 4c0-.6.4-1 1-1h3.5c.6 0 1 .4 1 1 0 1.3.2 2.5.6 3.6.1.3 0 .7-.2 1z"/></svg>
      </span>
      <span class="icon" aria-label="Cell phone">
        <svg width="20" height="20" viewBox="0 0 24 24"><rect x="6" y="2" width="12" height="20" rx="2" fill="none" stroke="#fff" stroke-width="2"/><circle cx="12" cy="18" r="1.2" fill="#fff"/></svg>
      </span>
      <span class="line"></span>
    </div>
    <p class="phones">555-287-4160<br>555-319-8274</p>
    <div class="rule"></div>
    <p class="address">238 W. Larkmoor Ave #310<br>Halden CA 90000</p>
    <div class="rule"></div>
    <p class="license"><span class="label">LIC</span> DRE 07461932</p>
  </article>

  <article class="card card-back">
    <div class="back-pattern" role="img" aria-label="Embossed repeating brand pattern in dark grey tones"></div>
    <div class="back-mark">
      <div class="brand-square"></div>
      <div class="brand-name"><span class="line-part">Bramwell Nest &amp; Lending</span></div>
    </div>
  </article>
</body>
</html>
```